Recruitment Site Design

We need a design for the login page, about page, and inner pages of a recruitment site for an oil and gas company. Design should be modern, sleek, professional and colors can be blue, green, white, orange or any other recommended colors.

Please also take into consideration that once the users login, they will need to access a form to fill in their information.

** UPDATE: Kindly provide a design for the inner information page consistent with the outer design. Attached is a picture of the basic structure. ***
Updates

Please provide a design for inner pages as shown in the design brief consistent with the registration page provided. 

Reason: We're extending it to get more inside pages.

Target Market(s)

Professionals looking for a career in the oil and gas industry in the Middle East.

Industry/Entity Type

Oil And Gas

Requirements
Must have
• Sleek design

```html
<!DOCTYPE html>
<html lang="en">
<head>
<meta charset="utf-8">
<title>Harbor Fuel Co. – Interior Page</title>
<link rel="stylesheet" href="https://fonts.googleapis.com/css2?family=Lato:ital,wght@0,300;0,400;0,700;0,900;1,300;1,400&display=swap">
<style>
  :root {
    --brand-blue: #1e6db5;
    --band-top: #2e8fd4;
    --band-bottom: #1c5fa5;
    --heading-blue: #2b7dc8;
    --text-grey: #6b6b6b;
    --quote-grey: #a3a3a3;
    --page-bg: #ebebeb;
    --white: #ffffff;
    --nav-grey: #8a8a8a;
    --rule-grey: #e2e2e2;
    --footer-bg: #131313;
    --orange-top: #ffc21a;
    --orange-bottom: #f08a00;
  }
  * { box-sizing: border-box; margin: 0; padding: 0; }
  html, body { width: 960px; height: 1200px; overflow: hidden; }
  body {
    position: relative;
    font-family: "Lato", Arial, sans-serif;
    color: var(--text-grey);
    background:
      radial-gradient(ellipse 520px 260px at 480px 420px, var(--white) 55%, transparent 100%),
      radial-gradient(ellipse 560px 300px at 480px 700px, var(--white) 50%, transparent 100%),
      var(--page-bg);
  }
  .abs { position: absolute; }

  /* Header */
  .site-header { left: 0; top: 0; width: 960px; height: 80px; background: var(--white); }
  .brand-name { left: 199px; top: 26px; font-size: 24px; font-weight: 900; color: var(--brand-blue); letter-spacing: -0.3px; }
  .main-nav a { position: absolute; top: 36px; font-size: 10px; font-weight: 700; color: var(--nav-grey); text-decoration: none; }
  .nav-divider { position: absolute; top: 28px; width: 1px; height: 32px; background: var(--rule-grey); }

  /* Title band */
  .title-band {
    left: 0; top: 80px; width: 960px; height: 77px;
    background: linear-gradient(var(--band-top), var(--band-bottom));
    border-top: 2px solid #4aa3e0;
  }
  .page-title { left: 197px; top: 106px; font-size: 20px; font-weight: 300; color: var(--white); }

  /* Intro */
  .pull-quote { left: 217px; top: 211px; width: 112px; font-size: 16px; line-height: 19.5px; font-style: italic; font-weight: 300; color: var(--quote-grey); }
  .quote-mark { font-family: Georgia, serif; font-size: 22px; color: var(--quote-grey); font-style: italic; }
  .body-copy { font-size: 10.6px; line-height: 14.3px; color: var(--text-grey); }
  .body-copy p + p { margin-top: 14px; }

  /* Video */
  .video-shadow { left: 200px; top: 578px; width: 320px; height: 30px;
    background: radial-gradient(ellipse at 50% 0, rgba(0,0,0,.35), transparent 70%); }
  .video-frame { left: 237px; top: 433px; width: 255px; height: 180px; background: var(--white);
    padding: 5px; box-shadow: 0 1px 4px rgba(0,0,0,.25); }
  .video-screen { width: 245px; height: 170px; display: block; }

  .small-copy { font-size: 8.7px; line-height: 14px; }

  .section-rule { left: 207px; top: 738px; width: 540px; height: 10px;
    background: radial-gradient(ellipse at 50% 0, rgba(0,0,0,.12), transparent 70%); }

  /* Feature columns */
  .feature { position: absolute; top: 786px; width: 160px; }
  .feature h2 { font-size: 20px; font-weight: 300; color: var(--heading-blue); margin-bottom: 12px; }
  .feature p { font-size: 7.6px; line-height: 11.3px; color: var(--text-grey); padding-left: 5px; width: 155px; }
  .more-button { display: inline-block; margin: 9px 0 0 4px; width: 36px; height: 13px; font-size: 7px; line-height: 13px;
    text-align: center; color: var(--white); border-radius: 2px; background: linear-gradient(#c9c9c9, #8d8d8d); }

  /* Footer */
  .site-footer { left: 0; top: 993px; width: 960px; height: 207px; background: var(--footer-bg); }
  .cta-box { left: 192px; top: 949px; width: 576px; height: 67px;
    background: linear-gradient(var(--white), #dedede); box-shadow: 0 2px 5px rgba(0,0,0,.25); }
  .cta-text { left: 31px; top: 22px; font-size: 19px; color: #333; }
  .cta-button { left: 424px; top: 19px; width: 132px; height: 32px; border-radius: 3px;
    background: linear-gradient(var(--orange-top), var(--orange-bottom));
    color: var(--white); font-size: 17px; font-weight: 700; text-align: center; line-height: 32px;
    box-shadow: 0 1px 2px rgba(0,0,0,.3); }
  .footer-links { left: 224px; top: 1077px; font-size: 9px; font-style: italic; color: var(--white); }
  .footer-links a { color: var(--white); text-decoration: none; }
  .footer-brand { right: 216px; top: 1056px; font-size: 22px; font-weight: 900; color: var(--brand-blue); }
  .legal-links { right: 220px; top: 1090px; font-size: 6px; color: var(--white); }
</style>
</head>
<body>
  <header class="site-header abs">
    <div class="brand-name abs">Harbor Fuel Co.</div>
    <nav class="main-nav">
      <a style="left:491px">Register</a>
      <span class="nav-divider" style="left:548px"></span>
      <a style="left:564px">Available Jobs</a>
      <span class="nav-divider" style="left:643px"></span>
      <a style="left:657px">FAQs</a>
      <span class="nav-divider" style="left:696px"></span>
      <a style="left:711px">Contact</a>
    </nav>
  </header>

  <div class="title-band abs"></div>
  <h1 class="page-title abs">Interior Page Title goes here</h1>

  <span class="quote-mark abs" style="left:193px;top:208px">“</span>
  <blockquote class="pull-quote abs">Duis aute irure dolor in reprehenderit in voluptate. Lorem ipsum dolor sit amet, consectetur adipisicing elit.</blockquote>
  <span class="quote-mark abs" style="left:325px;top:346px">”</span>

  <div class="body-copy abs" style="left:364px;top:204px;width:388px">
    <p>Duis aute irure dolor in reprehenderit in voluptate. Lorem ipsum dolor sit amet, consectetur adipisicing elit, sed do eiusmod tempor incididunt ut labore et dolore magna aliqua. Ut enim ad minim veniam, quis nostrud exercitation ullamco laboris nisi ut aliquip ex ea commodo consequat.</p>
    <p>Duis aute irure dolor in reprehenderit in voluptate. Lorem ipsum dolor sit amet, consectetur adipisicing elit, sed do eiusmod tempor incididunt ut labore et dolore magna aliqua. Ut enim ad minim veniam, quis nostrud exercitation ullamco laboris nisi ut aliquip ex ea commodo consequat. Duis aute irure dolor in reprehenderit in voluptate. Lorem ipsum dolor sit amet, consectetur adipisicing elit, sed do eiusmod tempor incididunt ut labore et dolore magna aliqua. Ut enim ad minim veniam, quis nostrud exercitation ullamco laboris nisi ut aliquip ex ea commodo consequat.</p>
  </div>

  <div class="video-shadow abs"></div>
  <div class="video-frame abs">
    <svg class="video-screen" viewBox="0 0 245 170" role="img" aria-label="Embedded video player">
      <defs>
        <radialGradient id="screen-glow" cx="50%" cy="45%" r="65%">
          <stop offset="0" stop-color="#5a5a5a"/><stop offset="1" stop-color="#2f2f2f"/>
        </radialGradient>
        <linearGradient id="play-face" x1="0" y1="0" x2="0" y2="1">
          <stop offset="0" stop-color="#d8d8d8"/><stop offset="1" stop-color="#8a8a8a"/>
        </linearGradient>
      </defs>
      <rect width="245" height="170" fill="url(#screen-glow)"/>
      <rect x="108" y="70" width="29" height="26" rx="4" fill="url(#play-face)"/>
      <path d="M118 76 L129 83 L118 90 Z" fill="#fff"/>
      <rect y="152" width="245" height="18" fill="#1a1a1a"/>
      <rect y="152" width="245" height="2" fill="#555"/>
      <circle cx="3" cy="153" r="2.5" fill="#ddd"/>
      <path d="M6 158 L11 161 L6 164 Z" fill="#bbb"/>
      <rect x="18" y="159" width="4" height="4" fill="#999"/>
      <text x="36" y="164" font-size="5" fill="#999" font-family="Lato, sans-serif">0:00 / 0:32</text>
      <rect x="212" y="158" width="7" height="5" fill="#c33"/>
      <rect x="234" y="158" width="6" height="5" fill="none" stroke="#999"/>
    </svg>
  </div>

  <div class="body-copy abs" style="left:545px;top:436px;width:190px">
    <p>Duis aute irure dolor in reprehenderit in voluptate. Lorem ipsum dolor sit amet, consectetur adipisicing elit, sed do eiusmod tempor incididunt ut labore et dolore magna aliqua. Ut enim ad minim veniam, quis nostrud exercitation ullamco laboris nisi ut aliquip ex ea commodo consequat. Duis aute irure dolor in reprehenderit in voluptate. Lorem ipsum dolor sit amet, consectetur adipisicing elit, sed do eiusmod tempor incididunt ut labore et dolore magna aliqua. Ut enim ad minim veniam, quis nostrud exercitation ullamco laboris nisi ut aliquip ex ea commodo consequat.</p>
  </div>

  <p class="small-copy abs" style="left:219px;top:649px;width:290px">Duis aute irure dolor in reprehenderit in voluptate. Lorem ipsum dolor sit amet, consectetur adipisicing elit, sed do eiusmod tempor incididunt ut labore et dolore magna aliqua. Ut enim ad minim veniam, quis nostrud exercitation ullamco laboris nisi ut aliquip ex ea commodo consequat.</p>

  <div class="section-rule abs"></div>

  <section class="feature" style="left:211px">
    <h2>Lorem Ipsum Elit</h2>
    <p>Lorem ipsum dolor sit amet, consectetur adipiscing elit. Curabitur lorem justo, euismod quis feugiat eu, malesuada eget erat. Class aptent taciti sociosqu ad litora torquent per conubia nostra, per inceptos himenaeos.</p>
    <span class="more-button">More</span>
  </section>
  <section class="feature" style="left:404px">
    <h2>Consectetur Elit</h2>
    <p>Lorem ipsum dolor sit amet, consectetur adipiscing elit. Curabitur lorem justo, euismod quis feugiat eu, malesuada eget erat. Class aptent taciti sociosqu ad litora torquent per conubia nostra, per inceptos himenaeos.</p>
    <span class="more-button">More</span>
  </section>
  <section class="feature" style="left:593px">
    <h2>Adipiscing Lorem</h2>
    <p>Lorem ipsum dolor sit amet, consectetur adipiscing elit. Curabitur lorem justo, euismod quis feugiat eu, malesuada eget erat. Class aptent taciti sociosqu ad litora torquent per conubia nostra, per inceptos himenaeos.</p>
    <span class="more-button">More</span>
  </section>

  <footer class="site-footer abs"></footer>
  <div class="cta-box abs">
    <div class="cta-text abs">Consectetur Elit Lorem Ipsum</div>
    <div class="cta-button abs">Register now</div>
  </div>

  <nav class="footer-links abs"><a>Home</a> | <a>Register</a> | <a>Available Jobs</a> | <a>FAQs</a> | <a>Contact</a></nav>
  <div class="footer-brand abs">Harbor Fuel Co.</div>
  <div class="legal-links abs">Terms of Use | Privacy Policy</div>
</body>
</html>
```